Mr T's - CD Cover Project number 6

Hi All,

I manage a small sound recording studio and need assistance with CD artwork, notably converting pdf image files to Photoshop, on print-ready templates, to submit to my CD duplication and packaging service

CD Name: “Roll On Home”, artist's name: “Mr. T’s Fine Tonic”.

In addition to the technical skill required to convert my images to Photoshop format, some creative design flair is desirable: the attractive superimposition of text (e.g., CD title and artist, liner notes, song titles, etc.) onto images, and the creation of professional-looking CD labels, is also required.

So I need a cover created using the images provided with the title and details superimposed.

I have planned on a folded rectangular insert to give 4 squarish pages – printed in color on one side of the rectangle, and monochromatic on the other.

I have executed this as a mock up, which you can view in 2 scans [ "...007jpg" and "...005.jpg" ]. Again, these scans are only of the mockup. (Source photos from which the mockups have been made are attached to this brie; others are available.)

The monochromatic side, once folded, would constitute the interior, i.e., where the text of the liner notes would be. It would be nice to see the text superimposed on a suitable background picture rendered lightly enough so as not to make the text difficult to read.

The color side would constitute the front "cover", or page 1 (visible through the plastic jewel case), and the back of the insert, or page 4. (The RIGHT-HAND SIDE of scan [“…007.jpeg”] would constitute the cover. The LEFT-HAND SIDE of the same scan would become the back of the insert.)

The name of the band [Mr. T’s Fine Tonic] , and the name of the CD [Roll On Home], would need to be added to page 1 (front cover, or RIGHT-HAND SIDE of scan [“…007.jpeg”] ) in some funky old (1920’s or 1930’s-style) font – without obscuring crucial parts of the various portraits.

(If a group portrait seems more suitable for the front cover than a collage of individual faces, a very good example is [ "Scan 110020032.jpeg" ] which could be substituted to advantage. This one already includes a likeness of the band's name.)

Pages 2 & 3 would consist of the text [see scan of mock up “.0005.jpg” ], i.e., the actual liner notes, provided in ".doc." file "ROLL ON HOME liner notes & song list.docx".

The song list, also contained in the ".doc" file, needs to be added to the back tray card, which is mocked up as scan “.00046.jpeg”.

The "Tarnished Fork Records" logo [see ".psd" file] also needs to go on the back tray card.

The name of the band and the name of the CD need also to go on the spine (edge).

An attractive, monochromatic CD label needs to be designed. I would like it to feature the name of the band and the song list, superimposed on a lightly-rendered background photo.

If more pix are requested/desirable, I would be happy to provide additional ones.

Guidelines for setup are provided by the duplication company, "Pressquay". These are available at http://pressquay.example-discworks.com/Quoter/Templates.aspx

Target Market(s)

All ages, all socioeconomic groups, who like to have a good time.

Industry/Entity Type

Recording Studio

Requirements
Must have
• A funky, old-fashioned feel. The music is all from the 1920's and 1930's - honky tonk, blues, and "jug band" style. Therefore fonts, and artistic treatments should be reflective of those times, not modern, new age, psychedelic, or anything suggestive of "rock & roll".
Nice to have
• A lightly-rendered picture as a background picture for superimposed liner notes.
Should not have
• Anything flashy, modern, hyper-abstract, or rock & roll-ish.

```html
<!DOCTYPE html>
<html lang="en">
<head>
<meta charset="utf-8">
<title>Mr. T’s Fine Tonic – Roll On Home – Back Tray Card</title>
<link rel="stylesheet" href="https://fonts.googleapis.com/css2?family=Rye&family=Alfa+Slab+One&display=swap">
<style>
  :root {
    --paper: #ffffff;
    --tray-green: #0f2d1b;
    --spine-yellow: #e8d62a;
    --track-red: #e0231c;
    --track-shadow: rgba(40, 10, 5, 0.85);
    --label-tan: #c9a27c;
    --label-cream: #e6d3bb;
    --photo-sky: #7f8f9c;
    --photo-shirt: #c7ccd6;
    --guide: #9a9a9a;
    --logo-ink: #e8e2d4;
  }
  html, body {
    margin: 0;
    padding: 0;
    width: 1200px;
    height: 1081px;
    overflow: hidden;
    background: var(--paper);
  }
  .canvas {
    position: relative;
    width: 1200px;
    height: 1081px;
    background: var(--paper);
  }
  .trim-guides {
    position: absolute;
    inset: 0;
  }
  .tray {
    position: absolute;
    left: 70px;
    top: 112px;
    width: 1078px;
    height: 849px;
    background: var(--tray-green);
  }
  .spine-text {
    position: absolute;
    font-family: "Alfa Slab One", serif;
    color: var(--spine-yellow);
    font-size: 22px;
    letter-spacing: 1px;
    white-space: nowrap;
    transform-origin: center;
  }
  .spine-left { transform: translate(-50%, -50%) rotate(-90deg); }
  .spine-right { transform: translate(-50%, -50%) rotate(90deg); }
  .medicine-label {
    position: absolute;
    left: 176px;
    top: 159px;
    width: 398px;
    height: 790px;
    background: linear-gradient(160deg, var(--label-cream) 0%, var(--label-tan) 55%, var(--label-cream) 100%);
  }
  .portrait-photo {
    position: absolute;
    left: 562px;
    top: 159px;
    width: 469px;
    height: 626px;
    background: linear-gradient(180deg, var(--photo-sky) 0%, #a99a8a 45%, var(--photo-shirt) 100%);
  }
  .track-list {
    position: absolute;
    left: 246px;
    top: 200px;
    margin: 0;
    padding: 0;
    list-style: none;
    font-family: "Rye", serif;
    font-size: 28px;
    line-height: 47.5px;
    color: var(--track-red);
    letter-spacing: 1.5px;
    text-shadow: 3px 4px 4px var(--track-shadow);
    white-space: nowrap;
  }
  .track-list .num {
    display: inline-block;
    min-width: 52px;
  }
  .label-mark {
    position: absolute;
    left: 922px;
    top: 812px;
    width: 112px;
    display: flex;
    align-items: center;
    gap: 8px;
  }
  .label-mark .square {
    width: 18px;
    height: 18px;
    flex: none;
    background: var(--logo-ink);
  }
  .label-mark .name {
    font-family: "Alfa Slab One", serif;
    font-size: 14px;
    line-height: 16px;
    color: var(--logo-ink);
  }
  .label-url {
    position: absolute;
    left: 870px;
    top: 893px;
    width: 215px;
    text-align: center;
    font-family: "Alfa Slab One", serif;
    font-size: 12px;
    letter-spacing: 1px;
    color: var(--track-red);
  }
</style>
</head>
<body>
<main class="canvas">
  <svg class="trim-guides" width="1200" height="1081" viewBox="0 0 1200 1081" aria-hidden="true">
    <g stroke="var(--guide)" stroke-width="1">
      <line x1="70.5" y1="0" x2="70.5" y2="95"/>
      <line x1="164.5" y1="0" x2="164.5" y2="95"/>
      <line x1="1043.5" y1="0" x2="1043.5" y2="95"/>
      <line x1="1147.5" y1="0" x2="1147.5" y2="95"/>
      <line x1="70.5" y1="978" x2="70.5" y2="1081"/>
      <line x1="164.5" y1="978" x2="164.5" y2="1081"/>
      <line x1="1043.5" y1="978" x2="1043.5" y2="1081"/>
      <line x1="1147.5" y1="978" x2="1147.5" y2="1081"/>
      <line x1="0" y1="112.5" x2="52" y2="112.5"/>
      <line x1="0" y1="960.5" x2="52" y2="960.5"/>
      <line x1="1166" y1="112.5" x2="1200" y2="112.5"/>
      <line x1="1166" y1="960.5" x2="1200" y2="960.5"/>
    </g>
  </svg>

  <section class="tray"></section>

  <div class="spine-text spine-left" style="left:117px; top:400px;">ROLL ON HOME</div>
  <div class="spine-text spine-left" style="left:117px; top:680px;">MR. T S FINE TONIC</div>
  <div class="spine-text spine-right" style="left:1095px; top:400px;">MR. T S FINE TONIC</div>
  <div class="spine-text spine-right" style="left:1095px; top:680px;">ROLL ON HOME</div>

  <div class="medicine-label" role="img" aria-label="Vintage tonic bottle label in sepia and cream tones"></div>
  <div class="portrait-photo" role="img" aria-label="Photograph of a band member in a pale fedora and shirt with braces"></div>

  <ol class="track-list">
    <li><span class="num">1.</span>Sunday Morning Blues</li>
    <li><span class="num">2.</span>Honey Pie</li>
    <li><span class="num">3.</span>Roll On Home</li>
    <li><span class="num">4.</span>Oh, Oh Brother Blues</li>
    <li><span class="num">5.</span>Tilly Burns</li>
    <li><span class="num">6.</span>Porch Step Rag</li>
    <li><span class="num">7.</span>Pick It Up Slow</li>
    <li><span class="num">8.</span>Sweet On My Darling</li>
    <li><span class="num">9.</span>Down the Line Again</li>
    <li><span class="num">10.</span>I Never Tried</li>
    <li><span class="num">11.</span>Old Mill Blues</li>
    <li><span class="num">12.</span>Find Me at the Station</li>
    <li><span class="num">13.</span>You’re Too Late</li>
    <li><span class="num">14.</span>Cousin Jane</li>
  </ol>

  <div class="label-mark">
    <span class="square"></span>
    <span class="name">Tarnished Fork Records</span>
  </div>
  <div class="label-url">WWW.TARNISHEDFORK.COM</div>
</main>
</body>
</html>
```